Our company needs a new modern concept for our webstore

Brindel Supplier Group is a product supply company supplying product for the building, architecture, interior design, printing and signage industries. We are looking for a clean, modern, corporate and sophisticated new look for our webstore.
The webstore should be PageForge and Ravo Basket based.
The webstore should include subtle and professional animations to enhance the look and catch the eye.
The Quince webstore is a good example to follow. We love the clean and simple yet highly sophisticated look of the Quince site. The homepage should start with a hero image at the top involving cladding and aluminium signage for corporate branding.
Underneath the hero image there should be a few lines of copy discussion the quality of our products (we will create the actual copy).
As the user scrolls past the few lines of copy they should come to our product categories represented by good quality end use images.
The product categories will be as follows:
Aluminium Panel – Ox Panel
Aluminium Composite Panel – Murt Panel
Acrylic Sheets – Temvoro
Print and Display
LED Lighting – Vesko LED Lighting
The brand logo for each of these product categories are attached to this brief. The logos should be used in the product categories in a clean, subtle but clear way.
There should be some subtle animation built into the product categories, such as the images expanding when hovering over or the logos animating onto the background images.

The home page navigation bar should appear at the very top above the hero image and should have the following buttons:
Home page
About page
Projects Gallery page
News
Contact page
Our main company logo Brindel Supplier Group is attached to this brief and should be shown small but clear at the top of the page either next to the navigation bar or in the middle of it.
The phone number 1300 458 903 should also be clearly shown at the top of the webstore.

For examples of the kinds of websites we like and level of clean, modern professionalism, see the links below:
https://www.quincegoods.example/store
https://www.plinthmedia.example.au/
https://www.corvanbuildworks.example.au/
https://tkrexteriors.example.au/

Industry/Entity Type

Architecture, Interior Design, Building, Shop fitting

Number of Pages Required

3 page

Font styles to use
Serif
Sans Serif

Requirements
Must have
• A clean, upmarket, modern and professional look that will appeal to architects and interior designers.
Nice to have
• An outstanding and slick website that promotes us as industry leaders for our products
Should not have
• A low market and cheap look that does not reflect the brand identify or its level of sophistication.

```html
<!DOCTYPE html>
<html lang="en">
<head>
<meta charset="utf-8">
<title>Brindel Supplier Group – Product Supply Company</title>
<link href="https://fonts.googleapis.com/css2?family=Poppins:wght@300;400;500;600;700&display=swap" rel="stylesheet">
<style>
:root{
  --plum:#7b1f4e;
  --plum-deep:#6e1a45;
  --nav:#3b3e46;
  --page:#f5f5f5;
  --white:#ffffff;
  --text:#555559;
  --ink:#2b2d33;
  --icon-orange:#f0a35c;
  --icon-red:#e0584a;
  --icon-blue:#7fb3e0;
  --icon-grey:#d3d6dc;
}
*{margin:0;padding:0;box-sizing:border-box}
html,body{width:1200px;height:3802px;overflow:hidden}
body{font-family:"Poppins",sans-serif;background:var(--page);color:var(--text);position:relative}
.abs{position:absolute}
.center{text-align:center;left:0;width:1200px}

/* Top navigation */
.topnav{top:0;left:0;width:1200px;height:49px;background:var(--nav)}
.topnav .brand{left:125px;top:15px;color:var(--white);font-weight:600;font-size:13px;letter-spacing:.4px}
.topnav .link{top:17px;color:var(--white);font-size:13px;letter-spacing:.6px}
.topnav .phone{top:16px;left:994px;color:var(--white);font-size:13px;letter-spacing:.6px;display:flex;align-items:center;gap:8px}
.tagline-bar{top:49px;left:0;width:1200px;height:71px;background:var(--white);text-align:center;line-height:71px;font-size:12px}
.tagline-bar b{color:var(--plum);font-weight:500}

/* Hero */
.hero{top:120px;left:0;width:1200px;height:562px;
  background:
    radial-gradient(ellipse 420px 300px at 1000px 200px,rgba(190,40,100,.45),transparent 70%),
    radial-gradient(ellipse 500px 200px at 300px 420px,rgba(70,20,50,.35),transparent 70%),
    linear-gradient(180deg,#8a3a66 0%,#9b3563 40%,#8c2b57 75%,#7a2950 100%)}
.hero h1{top:170px;font-size:70px;font-weight:700;color:var(--white);letter-spacing:-.5px}
.hero p{top:284px;font-size:22px;color:var(--white);line-height:34px}

/* Industries */
.industry{top:793px;width:170px;text-align:center}
.industry svg{display:block;margin:0 auto}
.industry span{display:block;margin-top:22px;color:var(--plum);font-size:16px}
.intro{top:980px;font-size:12.5px;line-height:25.5px;color:var(--text)}

/* Sections */
.section-title{font-size:44px;font-weight:600;color:var(--plum)}

/* Product cards */
.card{background:var(--white);border-radius:22px;overflow:hidden;box-shadow:0 4px 14px rgba(0,0,0,.05);transition:transform .4s ease,box-shadow .4s ease}
.card:hover{transform:translateY(-4px);box-shadow:0 10px 26px rgba(0,0,0,.09)}
.card .photo{width:100%;transition:transform .6s ease}
.card:hover .photo{transform:scale(1.05)}
.card .label{position:absolute;left:0;width:100%;text-align:center;font-weight:600;font-size:24px;color:#222}
.card .desc{position:absolute;left:0;width:100%;text-align:center;font-size:13px;line-height:25px;color:var(--text)}

/* Interior band */
.band{top:2266px;left:0;width:1200px;height:283px;
  background:
    radial-gradient(ellipse 260px 180px at 820px 120px,rgba(120,130,110,.25),transparent 70%),
    radial-gradient(ellipse 300px 200px at 330px 200px,rgba(110,100,90,.25),transparent 70%),
    linear-gradient(90deg,#44464c,#55575c 60%,#4a4c51)}
.band h2{top:78px;font-size:44px;font-weight:600;color:var(--white)}
.band p{top:158px;font-size:22px;line-height:34px;color:var(--white)}

/* Testimonial */
.quote-card{top:2804px;left:125px;width:939px;height:296px;background:var(--white);border-radius:30px}
.avatar{top:2757px;left:540px;width:110px;height:110px;border-radius:50%;background:radial-gradient(circle at 50% 45%,#c9a892,#8c6c5a 70%,#5d4a40);border:3px solid var(--white)}
.quote-text{top:2904px;font-size:16px;line-height:30px;color:var(--text)}
.quote-name{top:3010px;font-size:26px;font-weight:600;color:var(--plum)}
.quote-role{top:3052px;font-size:15px;color:#b5b5b5}
.arrow{width:48px;height:48px;border-radius:50%;background:var(--plum)}

/* Footer */
.footer{top:3330px;left:0;width:1200px;height:472px;background:var(--plum-deep);color:var(--white)}
.footer .brand{left:92px;top:80px;font-size:24px;font-weight:600;line-height:30px;width:220px}
.footer .about{left:92px;top:181px;font-size:12px;line-height:25px}
.social{top:274px;width:32px;height:32px;border-radius:50%;background:var(--white)}
.footer h4{top:92px;font-size:15px;font-weight:600}
.footer ul{list-style:none;top:138px;font-size:12px;line-height:20.7px}
.footer .contact li{display:flex;align-items:center;gap:12px}
.footer .rule{top:382px;left:96px;width:1018px;height:1px;background:rgba(255,255,255,.15)}
.footer .copy{top:396px;left:96px;font-size:12px}
.footer .legal{top:396px;right:86px;font-size:12px}
</style>
</head>
<body>

<header class="abs topnav">
  <div class="abs brand">Brindel Supplier Group</div>
  <a class="abs link" style="left:318px">Home</a>
  <a class="abs link" style="left:416px">About</a>
  <a class="abs link" style="left:515px">Projects Gallery</a>
  <a class="abs link" style="left:684px">News</a>
  <a class="abs link" style="left:778px">Contact</a>
  <div class="abs phone">
    <svg width="14" height="14" viewBox="0 0 24 24"><path fill="#fff" d="M6.6 10.8a15.1 15.1 0 0 0 6.6 6.6l2.2-2.2a1 1 0 0 1 1-.25 11.4 11.4 0 0 0 3.6.57 1 1 0 0 1 1 1V20a1 1 0 0 1-1 1A17 17 0 0 1 3 4a1 1 0 0 1 1-1h3.5a1 1 0 0 1 1 1c0 1.25.2 2.45.57 3.57a1 1 0 0 1-.25 1z"/></svg>
    1300 458 903
  </div>
</header>

<div class="abs tagline-bar"><b>Brindel Supplier Group</b> is a product supply company.</div>

<section class="abs hero" role="img" aria-label="Storefront with aluminium cladding and corporate signage under a magenta tint">
  <h1 class="abs center">Product Supply Company</h1>
  <p class="abs center">Brindel Supplier Group is a product supply company supplying product for the<br>building, architecture, interior design, printing and signage</p>
</section>

<!-- Industries -->
<div class="abs industry" style="left:181px">
  <svg width="68" height="68" viewBox="0 0 68 68" fill="none" stroke="#2b2d33" stroke-width="2" stroke-linejoin="round">
    <rect x="4" y="4" width="26" height="13" fill="#e0584a"/><rect x="34" y="4" width="30" height="13" fill="#f0a35c"/>
    <rect x="4" y="21" width="14" height="13" fill="#f0a35c"/><rect x="22" y="21" width="26" height="13" fill="#e0584a"/><rect x="52" y="21" width="12" height="13" fill="#f0a35c"/>
    <rect x="4" y="38" width="26" height="13" fill="#f0a35c"/><rect x="34" y="38" width="30" height="13" fill="#e0584a"/>
    <rect x="4" y="55" width="14" height="10" fill="#e0584a"/><rect x="22" y="55" width="26" height="10" fill="#f0a35c"/><rect x="52" y="55" width="12" height="10" fill="#e0584a"/>
  </svg>
  <span>Building</span>
</div>
<div class="abs industry" style="left:347px">
  <svg width="68" height="68" viewBox="0 0 68 68" fill="none" stroke="#2b2d33" stroke-width="2" stroke-linejoin="round">
    <rect x="6" y="2" width="56" height="8" fill="#f0a35c"/>
    <path d="M14 2v4M22 2v4M30 2v4M38 2v4M46 2v4M54 2v4"/>
    <rect x="4" y="14" width="60" height="48" rx="3" fill="#7fb3e0"/>
    <rect x="10" y="20" width="48" height="36" fill="#a9cdec"/>
    <path d="M18 26h32v24H18zM18 38h20M38 26v24M28 38v12"/>
  </svg>
  <span>Architecture</span>
</div>
<div class="abs industry" style="left:512px">
  <svg width="68" height="68" viewBox="0 0 68 68" fill="none" stroke="#2b2d33" stroke-width="2" stroke-linejoin="round">
    <rect x="4" y="6" width="22" height="58" fill="#d3d6dc"/>
    <path d="M4 20h22M4 34h22M4 48h22M12 13h6M12 27h6M12 41h6"/>
    <path d="M30 4h28v10H30z" fill="#7fb3e0"/><path d="M44 14v10"/>
    <rect x="30" y="24" width="34" height="40" fill="#ffffff"/>
    <rect x="36" y="44" width="22" height="14" fill="#e0584a"/><path d="M36 51h22M43 44v14M51 44v14"/>
    <path d="M36 30h22v8H36z" fill="#f0a35c"/>
  </svg>
  <span>Interior Design</span>
</div>
<div class="abs industry" style="left:675px">
  <svg width="68" height="68" viewBox="0 0 68 68" fill="none" stroke="#2b2d33" stroke-width="2" stroke-linejoin="round">
    <rect x="2" y="4" width="64" height="44" rx="3" fill="#7fb3e0"/>
    <rect x="8" y="10" width="52" height="32" fill="#d6e7f6"/>
    <path d="M34 16l10 5v11l-10 5-10-5V21z" fill="#f0a35c"/><path d="M24 21l10 5 10-5M34 26v11"/>
    <path d="M28 48l-3 10h18l-3-10"/><path d="M18 62h32" stroke-width="3"/>
  </svg>
  <span>Printing</span>
</div>
<div class="abs industry" style="left:837px">
  <svg width="68" height="68" viewBox="0 0 68 68" fill="none" stroke="#2b2d33" stroke-width="2" stroke-linejoin="round">
    <path d="M26 4h22v26H26z" fill="#d3d6dc"/><path d="M31 8v18M36 8v18M41 8v18"/>
    <path d="M20 12l6-6"/>
    <path d="M30 30v8M44 30v8"/>
    <rect x="18" y="38" width="36" height="18" fill="#e0584a"/>
    <rect x="24" y="43" width="10" height="8" fill="#f0a35c"/><rect x="38" y="43" width="10" height="8" fill="#f0a35c"/>
    <path d="M4 60h60" stroke-width="2.5"/><circle cx="10" cy="56" r="3" fill="#7fb3e0"/><circle cx="60" cy="56" r="3" fill="#7fb3e0"/>
  </svg>
  <span>Signage Industries</span>
</div>

<p class="abs center intro">Brindel Supplier Group is a product supply company supplying product for the building, architecture, interior design,<br>printing and signage industries. Brindel Supplier Group is a product supply company supplying product for the building,<br>architecture, interior design, printing and signage industries.</p>

<h2 class="abs center section-title" style="top:1140px">Product Categories</h2>

<article class="abs card" style="left:131px;top:1265px;width:288px;height:432px">
  <div class="photo" role="img" aria-label="Red shopfront facade on a narrow street" style="height:189px;background:
    radial-gradient(ellipse 90px 120px at 40px 140px,rgba(70,90,70,.7),transparent 70%),
    linear-gradient(180deg,rgba(255,255,255,.25),transparent 25%),
    linear-gradient(100deg,#c7303f 0%,#a81f33 45%,#c52b3a 70%,#7a1c28 100%)"></div>
  <div class="label" style="top:258px">Ox Panel</div>
  <div class="desc" style="top:334px">Company supplying product for<br>the building, architecture</div>
</article>
<article class="abs card" style="left:455px;top:1265px;width:287px;height:432px">
  <div class="photo" role="img" aria-label="Coffee shop exterior with timber cladding at night" style="height:189px;background:
    radial-gradient(ellipse 130px 40px at 150px 85px,rgba(255,220,170,.35),transparent 70%),
    linear-gradient(180deg,#7c7470 0%,#4a3b34 35%,#2a1e18 55%,#6c4429 75%,#8a5a34 100%)"></div>
  <div class="label" style="top:258px">Murt Panel</div>
  <div class="desc" style="top:334px">Company supplying product for<br>the building, architecture</div>
</article>
<article class="abs card" style="left:778px;top:1265px;width:288px;height:432px">
  <div class="photo" role="img" aria-label="Modern high-rise with blue glazed facade against the sky" style="height:189px;background:
    radial-gradient(ellipse 120px 110px at 260px 90px,rgba(235,242,248,.95),transparent 75%),
    linear-gradient(120deg,#1f3650 0%,#3d5f80 35%,#6f93b3 60%,#c9dae8 85%,#eef3f7 100%)"></div>
  <div class="label" style="top:258px">Temvoro</div>
  <div class="desc" style="top:334px">Company supplying product for<br>the building, architecture</div>
</article>
<article class="abs card" style="left:131px;top:1718px;width:451px;height:432px">
  <div class="photo" role="img" aria-label="Living room interior with beige sofa and round timber table" style="height:196px;background:
    radial-gradient(ellipse 170px 60px at 170px 150px,rgba(240,232,220,.8),transparent 70%),
    radial-gradient(ellipse 60px 40px at 140px 175px,rgba(170,120,75,.7),transparent 70%),
    linear-gradient(90deg,#d8d0c4 0%,#bdb0a0 35%,#8a7a68 60%,#4f4b44 80%,#6b6a5a 100%)"></div>
  <div class="label" style="top:262px">Brindel Supplier Group</div>
  <div class="desc" style="top:336px">Company supplying product for the building,<br>architecture interior design, printing</div>
</article>
<article class="abs card" style="left:616px;top:1718px;width:450px;height:432px">
  <div class="photo" role="img" aria-label="Timber-lined lounge interior with white sofa and garden windows" style="height:196px;background:
    radial-gradient(ellipse 120px 50px at 130px 140px,rgba(245,243,238,.9),transparent 70%),
    radial-gradient(ellipse 70px 70px at 240px 80px,rgba(120,150,90,.5),transparent 70%),
    linear-gradient(90deg,#a87a45 0%,#d8c6a8 25%,#ece8e1 45%,#c6a479 70%,#9a7244 100%)"></div>
  <div class="label" style="top:262px">Vesko LED Lighting</div>
  <div class="desc" style="top:336px">Company supplying product for the building,<br>architecture interior design, printing</div>
</article>

<section class="abs band" role="img" aria-label="Dimmed interior with chairs and plants">
  <h2 class="abs center">Interior Design</h2>
  <p class="abs center">Brindel Supplier Group is a product supply company supplying product for the<br>building, architecture, interior design, printing and signage</p>
</section>

<h2 class="abs center section-title" style="top:2652px">What Clients Say</h2>
<div class="abs quote-card"></div>
<div class="abs avatar" role="img" aria-label="Client portrait"></div>
<p class="abs center quote-text">Lorem ipsum dolor sit amet, consectetur adipisicing elit, sed do eiusmod tempor<br>incididunt ut labore et dolore magna aliqua. Ut enim ad minim</p>
<div class="abs center quote-name">Dalia R.</div>
<div class="abs center quote-role">Expert</div>
<div class="abs arrow" style="left:107px;top:2930px"><svg width="48" height="48" viewBox="0 0 48 48"><path d="M27 17l-7 7 7 7" fill="none" stroke="#fff" stroke-width="1.6"/></svg></div>
<div class="abs arrow" style="left:1036px;top:2930px"><svg width="48" height="48" viewBox="0 0 48 48"><path d="M21 17l7 7-7 7" fill="none" stroke="#fff" stroke-width="1.6"/></svg></div>
<svg class="abs" style="left:548px;top:3136px" width="86" height="68" viewBox="0 0 86 68" fill="none" stroke="#7b1f4e" stroke-width="2.2" stroke-linecap="round">
  <path d="M14 4c10 0 22 6 22 22 0 20-16 34-32 38 10-8 14-16 13-24C8 40 2 33 2 24 2 12 7 4 14 4z"/>
  <path d="M58 4c10 0 22 6 22 22 0 20-16 34-32 38 10-8 14-16 13-24-9 0-15-7-15-16 0-12 5-20 12-20z"/>
</svg>

<footer class="abs footer">
  <div class="abs brand">Brindel<br>Supplier Group</div>
  <p class="abs about">Lorem ipsum dolor sit amet, consectetur<br>adipisicing elit, sed do</p>
  <span class="abs social" style="left:93px"></span>
  <span class="abs social" style="left:135px"></span>
  <span class="abs social" style="left:176px"></span>
  <span class="abs social" style="left:219px"></span>

  <h4 class="abs" style="left:403px">Quick Links</h4>
  <ul class="abs" style="left:405px"><li>Home</li><li>About</li><li>Projects Gallery</li><li>News</li><li>Contact</li></ul>

  <h4 class="abs" style="left:599px">Services</h4>
  <ul class="abs" style="left:601px"><li>Aluminium Panel – Ox Panel</li><li>Aluminium Composite Panel – Murt Panel</li><li>Acrylic Sheets – Temvoro</li><li>Print and Display</li><li>LED Lighting – Vesko LED Lighting</li></ul>

  <h4 class="abs" style="left:917px">Contact Us</h4>
  <ul class="abs contact" style="left:917px">
    <li><svg width="14" height="14" viewBox="0 0 24 24"><path fill="none" stroke="#fff" stroke-width="1.6" d="M6.6 10.8a15.1 15.1 0 0 0 6.6 6.6l2.2-2.2a1 1 0 0 1 1-.25 11.4 11.4 0 0 0 3.6.57 1 1 0 0 1 1 1V20a1 1 0 0 1-1 1A17 17 0 0 1 3 4a1 1 0 0 1 1-1h3.5a1 1 0 0 1 1 1c0 1.25.2 2.45.57 3.57a1 1 0 0 1-.25 1z"/></svg>1300 458 903</li>
    <li><svg width="14" height="14" viewBox="0 0 24 24"><rect x="3" y="5" width="18" height="14" fill="none" stroke="#fff" stroke-width="1.6"/><path d="M3 5l9 8 9-8" fill="none" stroke="#fff" stroke-width="1.6"/></svg>info@brindelsupplier.example</li>
    <li style="margin-top:20px;align-items:flex-start"><svg width="14" height="14" viewBox="0 0 24 24"><path d="M12 2a7 7 0 0 0-7 7c0 5 7 13 7 13s7-8 7-13a7 7 0 0 0-7-7z" fill="none" stroke="#fff" stroke-width="1.6"/><circle cx="12" cy="9" r="2.5" fill="none" stroke="#fff" stroke-width="1.6"/></svg>MARROW<br>BAYSIDE</li>
  </ul>

  <div class="abs rule"></div>
  <div class="abs copy">Copyright © 2021 Brindel Supplier Group</div>
  <div class="abs legal">Privacy Policy | &nbsp;Terms of Use</div>
</footer>

</body>
</html>
```